Webpage

I am a professional genealogist. I need a webpage that is professional looking (using the logo I chose), I can add hyperlinks and photos to if and when I want.

```html
<!DOCTYPE html>
<html lang="en">
<head>
<meta charset="utf-8">
<title>Birchline Research Services</title>
<link href="https://fonts.googleapis.com/css2?family=Arimo:wght@400;700&family=Yanone+Kaffeesatz:wght@500&display=swap" rel="stylesheet">
<style>
:root{
  --teal:#12aec0;
  --green:#7dbb9d;
  --text:#8a8a8a;
  --dark:#444;
  --white:#fff;
}
*{margin:0;padding:0;box-sizing:border-box}
html,body{width:1200px;height:1156px;overflow:hidden;background:var(--white)}
body{position:relative;font-family:"Arimo",Arial,sans-serif;color:var(--text)}
a{color:inherit;text-decoration:none}
.abs{position:absolute}
.top-band{left:157px;top:0;width:886px;height:7px;background:var(--teal)}
.brand{left:157px;top:40px;display:flex;align-items:center;gap:12px}
.brand-mark{width:64px;height:64px;border-radius:50%;background:var(--green);opacity:.8}
.brand-name{font-size:22px;color:var(--dark);line-height:1}
.contact{right:157px;top:34px;text-align:right;font-size:13px;line-height:31px;color:var(--green)}
.contact .hl{color:var(--teal)}
.main-nav{left:157px;top:142px;width:886px;height:37px;background:var(--teal)}
.main-nav a{position:absolute;top:0;line-height:37px;color:var(--white);font-size:13.5px;transform:translateX(-50%)}
.hero{left:157px;top:179px;width:886px;height:466px;border-radius:0 0 16px 16px;
  background:radial-gradient(ellipse at 50% 40%,#8ed5b4 0%,#4e9c7c 50%,#1f5c45 100%);
  box-shadow:0 10px 14px -8px rgba(0,0,0,.25)}
.hero-title{left:0;right:0;top:34px;text-align:center;font-family:"Yanone Kaffeesatz",sans-serif;
  font-weight:500;font-size:56px;letter-spacing:1px;color:var(--white);text-shadow:0 0 2px #1aa2b5,0 0 3px #1aa2b5}
.dots{left:567px;top:667px;display:flex;gap:5px}
.dots span{width:13px;height:13px;border-radius:50%;background:#d4d4d4;border:1px solid #bbb}
.dots span.on{background:var(--green);border-color:var(--green)}
.col-title{top:728px;font-size:17px;color:var(--teal);font-weight:400}
.divider{top:729px;width:1px;height:236px;background:linear-gradient(transparent,#ddd 20%,#ddd 80%,transparent);box-shadow:1px 0 3px #eee}
.about-text{left:157px;top:780px;width:245px;font-size:12.5px;line-height:15.6px}
.about-text p+p{margin-top:15.6px}
.more{font-size:12.5px;color:var(--green)}
.services{left:470px;top:780px;list-style:none;font-size:13px;line-height:31px}
.services li{padding-left:16px;position:relative}
.services li::before{content:"";position:absolute;left:1px;top:12px;width:8px;height:8px;border-radius:50%;background:var(--green)}
.post{left:775px;width:267px;font-size:12.5px}
.post-meta{display:flex;justify-content:space-between;align-items:center;color:var(--dark);font-size:13px}
.post-meta span{display:flex;align-items:center;gap:8px}
.post-body{margin-top:20px;line-height:16px}
.post-body a{color:var(--green)}
.dotted{left:777px;top:860px;width:264px;border-top:1px dotted #999}
.view-all{left:774px;top:966px;font-size:13px;color:var(--green);border-bottom:1px solid var(--green)}
.footer-bar{left:157px;top:1029px;width:886px;height:44px;background:var(--green)}
.footer-nav{left:14px;top:0;line-height:44px;font-size:12.5px;color:var(--white)}
.footer-nav a+a::before{content:"| ";margin-left:2px}
.social{right:14px;top:10px;display:flex;gap:12px}
.social span{width:24px;height:24px;border-radius:50%;background:var(--white)}
.copyright{left:0;width:1200px;top:1103px;text-align:center;font-size:12px}
</style>
</head>
<body>
<div class="abs top-band"></div>

<header>
  <div class="abs brand"><span class="brand-mark"></span><span class="brand-name">Birchline Research Services</span></div>
  <address class="abs contact" style="font-style:normal">
    <div>Mara Ellison, <span class="hl">Professional Genealogist</span></div>
    <div>PO Box 5580 Austin, <span class="hl">TX 78700-1234</span></div>
    <div>512-555-0148, &nbsp;<a class="hl" href="#">mara@birchline.example</a></div>
  </address>
</header>

<nav class="abs main-nav">
  <a href="#" style="left:53px">Home</a>
  <a href="#" style="left:173px">About</a>
  <a href="#" style="left:302px">Services</a>
  <a href="#" style="left:437px">Contact</a>
  <a href="#" style="left:583px">Publications</a>
  <a href="#" style="left:719px">Blog</a>
  <a href="#" style="left:833px">Links</a>
</nav>

<section class="abs hero" role="img" aria-label="Green-tinted vintage family portrait of several generations posed together">
  <h1 class="abs hero-title">GENEALOGY RESEARCH</h1>
</section>
<div class="abs dots"><span class="on"></span><span></span><span></span><span></span></div>

<h2 class="abs col-title" style="left:157px">ABOUT ME</h2>
<div class="abs divider" style="left:435px"></div>
<h2 class="abs col-title" style="left:470px">OUR SERVICES</h2>
<div class="abs divider" style="left:739px"></div>
<h2 class="abs col-title" style="left:775px">OUR RECENT BLOG</h2>

<div class="abs about-text">
  <p>Lorem ipsum dolor sit amet, consectetur adipiscing elit. Phasellus id leo orci. Null am lacus mauris, gravida et enim in, ulla mcorper tristique sem. Morbi posuere m etus ipsum, sit amet interdum enim ferm entum ac. Aliquam consequat magna ma gna, ut rutrum lacus volutpat at.</p>
  <p>Mauris velit mauris, malesuada sed hend rerit sit amet, dignissim vel dui. Pellentes que elementum pharetra placerat.</p>
</div>
<a class="abs more" href="#" style="left:157px;top:966px">READ MORE [...]</a>

<ul class="abs services">
  <li>Forensic genealogy</li>
  <li>Kinship Determination</li>
  <li>Research analysis and Consultation</li>
  <li>Texas Researcher</li>
  <li>Record Retrieval</li>
</ul>
<a class="abs more" href="#" style="left:470px;top:942px">FIND MORE [...]</a>

<article class="abs post" style="top:781px">
  <div class="post-meta">
    <span><svg width="14" height="14" viewBox="0 0 14 14"><circle cx="7" cy="7" r="6" fill="none" stroke="#888" stroke-width="1.2"/><path d="M7 3.5V7h3" fill="none" stroke="#888" stroke-width="1.2"/></svg>MAY 8, 2014</span>
    <span><svg width="14" height="12" viewBox="0 0 14 12"><ellipse cx="7" cy="5" rx="6" ry="4" fill="#dfe9f7" stroke="#8aa8d8"/><path d="M4 8l-1 3 3-2" fill="#dfe9f7" stroke="#8aa8d8"/></svg>(0) Comments</span>
  </div>
  <p class="post-body">Lorem ipsum dolor sit amet, consectetur adip iscing elit. &nbsp;<a href="#">read more [...]</a></p>
</article>
<div class="abs dotted"></div>
<article class="abs post" style="top:873px">
  <div class="post-meta">
    <span><svg width="14" height="14" viewBox="0 0 14 14"><circle cx="7" cy="7" r="6" fill="none" stroke="#888" stroke-width="1.2"/><path d="M7 3.5V7h3" fill="none" stroke="#888" stroke-width="1.2"/></svg>May 28, 2014</span>
    <span><svg width="14" height="12" viewBox="0 0 14 12"><ellipse cx="7" cy="5" rx="6" ry="4" fill="#dfe9f7" stroke="#8aa8d8"/><path d="M4 8l-1 3 3-2" fill="#dfe9f7" stroke="#8aa8d8"/></svg>(0) Comments</span>
  </div>
  <p class="post-body">Lorem ipsum dolor sit amet, consectetur adip iscing elit. &nbsp;<a href="#">read more [...]</a></p>
</article>
<a class="abs view-all" href="#">VIEW ALL</a>

<footer>
  <div class="abs footer-bar">
    <nav class="abs footer-nav">
      <a href="#">Home</a> <a href="#">About</a> <a href="#">Services</a> <a href="#">Contact</a> <a href="#">Publications</a> <a href="#">Blog</a> <a href="#">Links</a>
    </nav>
    <div class="abs social" aria-label="Social links"><span></span><span></span><span></span><span></span></div>
  </div>
  <p class="abs copyright">© Birchline Research Services 2014. All rights reserved.</p>
</footer>
</body>
</html>
```